Business cards for KORU Real Estate Holdings LLC

We need a cool, original business card design for a company based in the Washington DC metropolitan area. We are a new energetic and passionate Real Estate Investing Company that invests in all types of real estate; commercial, residential, industrial etc.

Our company color is Red since it reflects action, energy and speed; it is assertive confident, energizing, exciting, powerful, passionate and determined. So we would like business card communicate those qualities to the audience.

Our audiences are investors that want to invest with us, real estate sellers, buyers, and tenants who lease from us.

Our logo is attached

```html
<!DOCTYPE html>
<html lang="en">
<head>
<meta charset="utf-8">
<title>KORU Real Estate Holdings LLC – Business Cards</title>
<link rel="stylesheet" href="https://fonts.googleapis.com/css2?family=Cinzel:wght@400&family=Open+Sans:wght@700;800&family=Questrial&display=swap">
<style>
  :root {
    --stage: #2b2b2d;
    --card-white: #ffffff;
    --card-shade: #e9e9ea;
    --brand-red: #c8161d;
    --ink: #1c1c1c;
    --ink-soft: #3a3a3a;
    --edge-black: #111111;
  }
  * { margin: 0; padding: 0; box-sizing: border-box; }
  html, body {
    width: 1200px; height: 900px; overflow: hidden;
    background: var(--stage);
  }
  .stage { position: relative; width: 1200px; height: 900px; }

  .card {
    position: absolute;
    width: 700px; height: 400px;
    background: linear-gradient(160deg, var(--card-white) 30%, var(--card-shade) 100%);
    box-shadow: 0 14px 30px rgba(0,0,0,.55);
    overflow: hidden;
  }
  .card--back { left: 90px; top: 40px; }
  .card--front { left: 410px; top: 465px; }

  .card__edge { position: absolute; left: 0; bottom: 0; width: 700px; height: 70px; }

  .wordmark {
    position: absolute;
    display: flex; align-items: center; gap: 14px;
    font-family: "Open Sans", sans-serif; font-weight: 800;
    color: var(--ink);
    font-size: 30px; letter-spacing: .5px; line-height: 1.05;
  }
  .wordmark__square { width: 38px; height: 38px; background: var(--brand-red); flex: none; }
  .card--back .wordmark { left: 150px; top: 105px; }
  .card--front .wordmark { left: 170px; top: 55px; }

  .tagline {
    position: absolute; left: 60px; top: 262px;
    font-family: "Open Sans", sans-serif; font-weight: 800;
    font-size: 19px; letter-spacing: 2.5px; color: var(--ink);
  }

  .holder {
    position: absolute; right: 48px; top: 150px; text-align: right;
    font-family: "Cinzel", serif;
  }
  .holder__name { font-size: 27px; color: var(--brand-red); line-height: 1.1; }
  .holder__role { font-size: 17px; color: var(--ink-soft); letter-spacing: 1px; }

  .contact-rail {
    position: absolute; left: 22px; top: 205px;
    width: 52px; height: 160px;
    background: var(--brand-red); border-radius: 0 10px 10px 0;
    display: flex; flex-direction: column; justify-content: space-around; align-items: center;
    padding: 8px 0;
  }
  .contact-rail svg { width: 24px; height: 24px; }

  .contact-list {
    position: absolute; left: 100px; top: 203px;
    font-family: "Questrial", sans-serif; font-size: 21px; color: var(--ink);
    list-style: none; line-height: 1.2;
  }
  .contact-list li { margin-bottom: 10px; }
</style>
</head>
<body>
<main class="stage">

  <section class="card card--back" aria-label="Card back">
    <div class="wordmark"><span class="wordmark__square"></span><span>KORU Real Estate<br>Holdings LLC</span></div>
    <p class="tagline">REAL ESTATE, COMMERCIAL, RESIDENTIAL, INDUSTRIAL</p>
    <svg class="card__edge" viewBox="0 0 700 70" aria-hidden="true">
      <path d="M0 56 L540 56 Q552 56 558 46 L566 30 Q572 20 584 20 L700 20 L700 70 L0 70 Z" fill="var(--edge-black)"/>
      <path d="M0 56 L540 56 Q552 56 558 46 L562 38 L562 70 L0 70 Z" fill="var(--brand-red)"/>
    </svg>
  </section>

  <section class="card card--front" aria-label="Card front">
    <div class="wordmark"><span class="wordmark__square"></span><span>KORU Real Estate<br>Holdings LLC</span></div>

    <div class="holder">
      <p class="holder__name">YOUR NAME</p>
      <p class="holder__role">DESIGNATION</p>
    </div>

    <div class="contact-rail" aria-hidden="true">
      <svg viewBox="0 0 24 24"><path d="M6 3 L9 3 L10 8 L8 9.5 Q10 14 14.5 16 L16 14 L21 15 L21 18 Q21 21 18 21 Q4 19 3 6 Q3 3 6 3 Z" fill="#fff"/></svg>
      <svg viewBox="0 0 24 24"><rect x="6" y="2" width="12" height="7" fill="#fff"/><rect x="3" y="10" width="18" height="9" rx="1.5" fill="#fff"/><rect x="7" y="16" width="10" height="6" fill="#fff" stroke="var(--brand-red)" stroke-width="1.2"/></svg>
      <svg viewBox="0 0 24 24"><rect x="2" y="5" width="20" height="14" fill="#fff"/><path d="M2 5 L12 13 L22 5" fill="none" stroke="var(--brand-red)" stroke-width="1.5"/></svg>
      <svg viewBox="0 0 24 24"><path d="M12 2 Q19 2 19 9 Q19 14 12 22 Q5 14 5 9 Q5 2 12 2 Z" fill="#fff"/><circle cx="12" cy="9" r="3" fill="var(--brand-red)"/></svg>
    </div>

    <ul class="contact-list">
      <li>07 41635502</li>
      <li>07 41635519</li>
      <li>Info@koru-holdings.com</li>
      <li>Your Complete<br>Address Details Here</li>
    </ul>

    <svg class="card__edge" viewBox="0 0 700 70" aria-hidden="true">
      <path d="M0 56 L540 56 Q552 56 558 46 L566 30 Q572 20 584 20 L700 20 L700 70 L0 70 Z" fill="var(--edge-black)"/>
      <path d="M0 56 L540 56 Q552 56 558 46 L562 38 L562 70 L0 70 Z" fill="var(--brand-red)"/>
    </svg>
  </section>

</main>
</body>
</html>
```